Bar and Grill needs specials signage

I have attached a file called "daily specials" I need it changed - so there is 1 sign/poster for each day/special
also attached other items to show some styling. I want the new posters chalkboard format, styled along the lines of the drink designs attached.
The designs should be scaleable, and editable, I will print locally

```html
<!DOCTYPE html>
<html lang="en">
<head>
<meta charset="utf-8">
<title>Daily Specials – Chalkboard Posters</title>
<link rel="stylesheet" href="https://fonts.googleapis.com/css2?family=Playball&family=Oranienbaum&family=Graduate&family=Sancreek&family=Amatic+SC:wght@700&family=Fira+Sans+Condensed:wght@600&family=Courgette&display=swap">
<style>
  :root {
    --stage: #5f5f5f;
    --board-dark: #1c1c1c;
    --board-mid: #2c2c2c;
    --board-haze: rgba(255, 255, 255, 0.07);
    --chalk-white: #f4f1ea;
    --chalk-line: rgba(244, 241, 234, 0.78);
    --chalk-yellow: #ece08e;
    --chalk-salmon: #f2897a;
    --shadow: rgba(0, 0, 0, 0.5);
  }
  * { box-sizing: border-box; margin: 0; padding: 0; }
  html, body {
    width: 1200px; height: 640px; overflow: hidden;
    background: var(--stage);
  }
  .filter-defs { position: absolute; width: 0; height: 0; }
  .stage { position: relative; width: 1200px; height: 640px; }

  .poster {
    position: absolute; top: 90px;
    width: 355px; height: 459px;
    overflow: hidden;
    background:
      radial-gradient(ellipse 60% 35% at 25% 15%, var(--board-haze), transparent 70%),
      radial-gradient(ellipse 55% 30% at 70% 55%, rgba(255,255,255,0.05), transparent 70%),
      radial-gradient(ellipse 50% 30% at 35% 88%, rgba(255,255,255,0.05), transparent 70%),
      linear-gradient(165deg, var(--board-mid), var(--board-dark));
    box-shadow: 3px 4px 7px var(--shadow);
    color: var(--chalk-white);
    text-align: center;
  }
  .poster--monday { left: 183px; }
  .poster--tuesday { left: 662px; }

  .poster__grain, .poster__art { position: absolute; inset: 0; width: 355px; height: 459px; }
  .poster__art { filter: url(#chalk-stroke); }
  .poster__art .rule { fill: none; stroke: var(--chalk-line); stroke-width: 1.4; stroke-linecap: round; }
  .poster__art .rule--thin { stroke-width: 1; opacity: 0.7; }
  .poster__art .ticks { fill: none; stroke-width: 3.5; stroke-dasharray: 1.2 3.2; }
  .poster__art .ticks--yellow { stroke: var(--chalk-yellow); }
  .poster__art .ticks--white { stroke: var(--chalk-line); }
  .poster__art .ticks--salmon { stroke: var(--chalk-salmon); stroke-width: 4; stroke-dasharray: 1.4 4.6; }
  .banner-title {
    font-family: "Oranienbaum", serif;
    font-size: 44px;
    fill: var(--chalk-white);
  }

  .line { position: absolute; left: 0; right: 0; line-height: 1; white-space: nowrap; filter: url(#chalk-text); }

  .title-script {
    top: 8px;
    font-family: "Playball", cursive;
    font-size: 50px;
  }

  .cutlery {
    position: absolute; left: 161px; top: 104px;
    width: 30px; height: 50px;
    border-radius: 8px;
    background: radial-gradient(ellipse at center, rgba(244,241,234,0.35), rgba(244,241,234,0.05) 75%, transparent);
  }

  .day {
    font-family: "Graduate", serif;
    font-weight: 400;
  }
  .day--monday { top: 157px; font-size: 56px; color: var(--chalk-yellow); }
  .day--tuesday { top: 161px; font-size: 44px; letter-spacing: 6px; padding-left: 6px; color: var(--chalk-salmon); }

  .offer-western {
    top: 240px;
    font-family: "Sancreek", serif;
    font-size: 37px;
    color: var(--chalk-yellow);
  }
  .offer-detail {
    font-family: "Amatic SC", sans-serif;
    font-weight: 700;
    font-size: 30px; letter-spacing: 2px;
  }
  .offer-detail--first { top: 289px; }
  .offer-detail--second { top: 321px; }

  .offer-bold {
    top: 246px;
    font-family: "Fira Sans Condensed", sans-serif;
    font-weight: 600;
    font-size: 42px;
  }
  .offer-time {
    top: 296px;
    font-family: "Courgette", cursive;
    font-size: 23px;
  }

  .illustration { position: absolute; border-radius: 30px; }
  .illustration--kids-food {
    left: 109px; top: 374px; width: 148px; height: 71px;
    background: radial-gradient(ellipse at center, rgba(236,224,142,0.32), rgba(244,241,234,0.1) 60%, transparent 80%);
  }
  .illustration--wings {
    left: 58px; top: 338px; width: 236px; height: 104px;
    background: radial-gradient(ellipse at center, rgba(242,137,122,0.3), rgba(244,241,234,0.08) 60%, transparent 80%);
  }
</style>
</head>
<body>
<svg class="filter-defs" aria-hidden="true">
  <defs>
    <filter id="board-grain" x="0" y="0" width="100%" height="100%">
      <feTurbulence type="fractalNoise" baseFrequency="0.75" numOctaves="3" seed="4"/>
      <feColorMatrix type="matrix" values="0 0 0 0 1  0 0 0 0 1  0 0 0 0 1  0 0 0 0.22 -0.06"/>
    </filter>
    <filter id="chalk-text" x="-5%" y="-10%" width="110%" height="120%">
      <feTurbulence type="fractalNoise" baseFrequency="0.9" numOctaves="2" seed="7" result="noise"/>
      <feDisplacementMap in="SourceGraphic" in2="noise" scale="1.6" xChannelSelector="R" yChannelSelector="G" result="rough"/>
      <feColorMatrix in="noise" type="matrix" values="0 0 0 0 0  0 0 0 0 0  0 0 0 0 0  0 0 0 -2.4 2.05" result="speckle"/>
      <feComposite in="rough" in2="speckle" operator="in"/>
    </filter>
    <filter id="chalk-stroke" x="0" y="0" width="100%" height="100%">
      <feTurbulence type="fractalNoise" baseFrequency="0.8" numOctaves="2" seed="2" result="noise"/>
      <feDisplacementMap in="SourceGraphic" in2="noise" scale="2" xChannelSelector="R" yChannelSelector="G" result="rough"/>
      <feColorMatrix in="noise" type="matrix" values="0 0 0 0 0  0 0 0 0 0  0 0 0 0 0  0 0 0 -2 1.8" result="speckle"/>
      <feComposite in="rough" in2="speckle" operator="in"/>
    </filter>
    <mask id="behind-script" maskUnits="userSpaceOnUse" x="0" y="0" width="355" height="459">
      <rect width="355" height="459" fill="#fff"/>
      <rect x="112" y="8" width="130" height="62" fill="#000"/>
    </mask>
    <path id="banner-curve" d="M95 112 Q177 96 259 112"/>
  </defs>
</svg>

<main class="stage">

  <section class="poster poster--monday">
    <svg class="poster__grain" viewBox="0 0 355 459" aria-hidden="true"><rect width="355" height="459" filter="url(#board-grain)"/></svg>
    <svg class="poster__art" viewBox="0 0 355 459" aria-hidden="true">
      <path class="rule" d="M18 142 V24 H62"/><path class="rule rule--thin" d="M26 134 V36 Q26 30 32 30 H56"/>
      <path class="rule" d="M337 142 V24 H293"/><path class="rule rule--thin" d="M329 134 V36 Q329 30 323 30 H299"/>
      <path class="rule" d="M18 376 V440 H62"/><path class="rule rule--thin" d="M26 384 V428 Q26 434 32 434 H56"/>
      <path class="rule" d="M337 376 V440 H293"/><path class="rule rule--thin" d="M329 384 V428 Q329 434 323 434 H299"/>
      <path class="rule" d="M24 152 V360"/><path class="rule" d="M331 152 V360"/>
      <path class="rule" mask="url(#behind-script)" d="M53 74 Q177 38 301 74"/>
      <path class="rule" d="M53 74 L97 114"/><path class="rule" d="M301 74 L257 114"/>
      <path class="rule rule--thin" d="M62 80 L100 110"/><path class="rule rule--thin" d="M292 80 L254 110"/>
      <text class="banner-title"><textPath href="#banner-curve" startOffset="50%" text-anchor="middle" textLength="150" lengthAdjust="spacingAndGlyphs">SPECIALS</textPath></text>
      <path class="ticks ticks--yellow" d="M101 120 H153"/><path class="ticks ticks--yellow" d="M199 120 H253"/>
      <path class="rule" d="M21 149 H333"/>
      <path class="rule" d="M21 221 H333"/>
      <path class="ticks ticks--white" d="M52 302 H94"/><path class="ticks ticks--white" d="M260 302 H302"/>
      <path class="ticks ticks--yellow" d="M53 364 H303"/>
    </svg>
    <p class="line title-script">Daily</p>
    <div class="cutlery" role="img" aria-label="Chalk drawing of spoon, fork and knife"></div>
    <h2 class="line day day--monday">MONDAY</h2>
    <p class="line offer-western">KIDS EAT FREE</p>
    <p class="line offer-detail offer-detail--first">FROM OUR MENU</p>
    <p class="line offer-detail offer-detail--second">WITH ADULT PURCHASE</p>
    <div class="illustration illustration--kids-food" role="img" aria-label="Chalk drawings of an ice cream cone, a burger and fries"></div>
  </section>

  <section class="poster poster--tuesday">
    <svg class="poster__grain" viewBox="0 0 355 459" aria-hidden="true"><rect width="355" height="459" filter="url(#board-grain)"/></svg>
    <svg class="poster__art" viewBox="0 0 355 459" aria-hidden="true">
      <path class="rule" d="M18 142 V24 H62"/><path class="rule rule--thin" d="M26 134 V36 Q26 30 32 30 H56"/>
      <path class="rule" d="M337 142 V24 H293"/><path class="rule rule--thin" d="M329 134 V36 Q329 30 323 30 H299"/>
      <path class="rule" d="M18 376 V440 H62"/><path class="rule rule--thin" d="M26 384 V428 Q26 434 32 434 H56"/>
      <path class="rule" d="M337 376 V440 H293"/><path class="rule rule--thin" d="M329 384 V428 Q329 434 323 434 H299"/>
      <path class="rule" d="M24 152 V360"/><path class="rule" d="M331 152 V360"/>
      <path class="rule" mask="url(#behind-script)" d="M53 74 Q177 38 301 74"/>
      <path class="rule" d="M53 74 L97 114"/><path class="rule" d="M301 74 L257 114"/>
      <path class="rule rule--thin" d="M62 80 L100 110"/><path class="rule rule--thin" d="M292 80 L254 110"/>
      <text class="banner-title"><textPath href="#banner-curve" startOffset="50%" text-anchor="middle" textLength="150" lengthAdjust="spacingAndGlyphs">SPECIALS</textPath></text>
      <path class="ticks ticks--white" d="M101 120 H153"/><path class="ticks ticks--white" d="M199 120 H253"/>
      <path class="rule" d="M21 149 H333"/>
      <path class="ticks ticks--salmon" d="M54 234 H302"/>
      <path class="ticks ticks--salmon" d="M50 306 H94"/><path class="ticks ticks--salmon" d="M258 306 H302"/>
    </svg>
    <p class="line title-script">Daily</p>
    <div class="cutlery" role="img" aria-label="Chalk drawing of spoon, fork and knife"></div>
    <h2 class="line day day--tuesday">TUESDAY</h2>
    <p class="line offer-bold">55 cent WINGS</p>
    <p class="line offer-time">After 3:00 pm</p>
    <div class="illustration illustration--wings" role="img" aria-label="Chalk drawings of two hens beside a steaming basket of wings"></div>
  </section>

</main>
</body>
</html>
```